Business Card and Word .doc header and footer required

I need a business card designed for my cybersecurity consulting company. Also required, is a header and footer to be ued for my word documents.
Attached is the Logo design, font and rgb used.

Industry/Entity Type

Cyber Security Consulting

Contact Information for Business Card

Name, Phone, email, website

Colors
0054AA
0677BA
7BADD7
CADEEF
E8F1F8

Requirements
Must have
• Sleek, modern

```html
<!DOCTYPE html>
<html lang="en">
<head>
<meta charset="utf-8">
<title>Harlow Ridge Consulting – Stationery</title>
<link rel="stylesheet" href="https://fonts.googleapis.com/css2?family=Montserrat:wght@500;600;700&family=Open+Sans:wght@400;600&display=swap">
<style>
  :root {
    --stage: #c3c4c6;
    --navy: #0b1120;
    --blue: #0677ba;
    --blue-deep: #0054aa;
    --blue-light: #7badd7;
    --paper: #ffffff;
    --ghost: #eeeff1;
    --text: #3a3f4a;
    --rule: #c9ccd2;
  }
  * { box-sizing: border-box; margin: 0; padding: 0; }
  html, body { width: 1200px; height: 1200px; overflow: hidden; }
  body { background: var(--stage); font-family: "Open Sans", Arial, sans-serif; position: relative; }

  .letterhead { position: absolute; z-index: 1; left: 360px; top: 88px; width: 791px; height: 1023px; background: var(--paper); overflow: hidden; box-shadow: 0 4px 14px rgba(0,0,0,.18); }
  .letterhead__art, .card__art { position: absolute; inset: 0; }
  .brand-name { font-family: "Montserrat", Arial, sans-serif; font-weight: 600; color: var(--paper); text-align: center; letter-spacing: .3px; line-height: 1.15; }
  .brand-name--dark { color: var(--navy); }
  .letterhead__brand { position: absolute; left: 179px; top: 22px; width: 220px; font-size: 22px; }
  .brand-mark { display: block; margin: 0 auto 8px; border-radius: 50%; border: 3px solid var(--blue); }
  .letterhead__contact { position: absolute; left: 425px; top: 48px; width: 160px; color: #e6ebf2; font-size: 11.5px; }
  .contact-line { display: flex; align-items: center; gap: 6px; height: 18px; white-space: nowrap; }
  .contact-line svg { flex: none; }
  .contact-rule { height: 1px; background: #56607a; margin: 6px 0 10px; width: 140px; }

  .card { position: absolute; z-index: 2; width: 375px; height: 215px; background: var(--paper); overflow: hidden; box-shadow: 0 4px 12px rgba(0,0,0,.22); }
  .card--front { left: 67px; top: 417px; }
  .card--back { left: 113px; top: 781px; }
  .card__brand { position: absolute; left: 6px; top: 66px; width: 130px; font-size: 14px; }
  .card__person { position: absolute; left: 176px; top: 48px; color: var(--text); font-size: 11px; }
  .card__role { font-size: 11px; color: var(--text); }
  .card__name { font-family: "Montserrat", Arial, sans-serif; font-weight: 600; color: var(--blue); font-size: 14px; letter-spacing: .3px; margin-bottom: 2px; }
  .card__person .contact-line { height: 16px; color: var(--text); font-size: 10.5px; }
  .card__rule { width: 125px; height: 1px; background: var(--rule); margin: 8px 0 18px; }
  .card--back .card__brand { left: 67px; top: 46px; width: 240px; font-size: 22px; }
</style>
</head>
<body>
  <section class="letterhead" aria-label="Letterhead">
    <svg class="letterhead__art" viewBox="0 0 791 1023" aria-hidden="true">
      <circle cx="417" cy="662" r="360" fill="none" stroke="var(--ghost)" stroke-width="34"/>
      <path d="M0 0 H791 V93 Q395.5 273 0 93 Z" fill="var(--navy)"/>
      <path d="M0 97 Q395.5 280 791 97" fill="none" stroke="var(--blue)" stroke-width="4"/>
      <rect x="0" y="974" width="791" height="4" fill="var(--blue)"/>
      <rect x="0" y="980" width="791" height="43" fill="var(--navy)"/>
    </svg>
    <div class="letterhead__brand brand-name">
      <span class="brand-mark" style="width:50px;height:50px"></span>
      Harlow Ridge Consulting
    </div>
    <div class="letterhead__contact">
      <div class="contact-line">
        <svg width="8" height="9" viewBox="0 0 8 9"><path d="M1 0h2l1 2-1 1a5 5 0 0 0 2 3l1-1 2 1v2l-1 1C3 9 0 5 0 1z" fill="var(--blue-light)"/></svg>
        555-204-7316
      </div>
      <div class="contact-rule"></div>
      <div class="contact-line">
        <svg width="9" height="7" viewBox="0 0 9 7"><rect width="9" height="7" rx="1" fill="var(--blue-light)"/></svg>
        daniel@harlowridge.com
      </div>
      <div class="contact-line">
        <svg width="9" height="9" viewBox="0 0 9 9"><circle cx="4.5" cy="4.5" r="4.5" fill="var(--blue-light)"/></svg>
        www.harlowridge.com
      </div>
    </div>
  </section>

  <section class="card card--front" aria-label="Business card front">
    <svg class="card__art" viewBox="0 0 375 215" aria-hidden="true">
      <circle cx="70" cy="120" r="120" fill="none" stroke="var(--ghost)" stroke-width="16"/>
      <path d="M0 0 H135 Q180 107.5 135 215 H0 Z" fill="var(--navy)"/>
      <path d="M135 0 Q180 107.5 135 215" fill="none" stroke="var(--blue)" stroke-width="2.5"/>
      <rect x="360" y="0" width="15" height="215" fill="var(--navy)"/>
      <rect x="356" y="0" width="2.5" height="215" fill="var(--blue)"/>
    </svg>
    <div class="card__brand brand-name">
      <span class="brand-mark" style="width:34px;height:34px"></span>
      Harlow Ridge Consulting
    </div>
    <div class="card__person">
      <div class="card__role">Director</div>
      <div class="card__name">DANIEL REYES</div>
      <div class="contact-line">
        <svg width="8" height="9" viewBox="0 0 8 9"><path d="M1 0h2l1 2-1 1a5 5 0 0 0 2 3l1-1 2 1v2l-1 1C3 9 0 5 0 1z" fill="var(--navy)"/></svg>
        555-204-7316
      </div>
      <div class="card__rule"></div>
      <div class="contact-line">
        <svg width="9" height="7" viewBox="0 0 9 7"><rect width="9" height="7" rx="1" fill="var(--navy)"/></svg>
        daniel@harlowridge.com
      </div>
      <div class="contact-line">
        <svg width="9" height="9" viewBox="0 0 9 9"><circle cx="4.5" cy="4.5" r="4.5" fill="var(--navy)"/></svg>
        www.harlowridge.com
      </div>
    </div>
  </section>

  <section class="card card--back" aria-label="Business card back">
    <svg class="card__art" viewBox="0 0 375 215" aria-hidden="true">
      <circle cx="150" cy="120" r="140" fill="none" stroke="var(--ghost)" stroke-width="16"/>
    </svg>
    <div class="card__brand brand-name brand-name--dark">
      <span class="brand-mark" style="width:44px;height:44px"></span>
      Harlow Ridge Consulting
    </div>
  </section>
</body>
</html>
```